Namecard Designs+Logo for a High End Automobile Company

We need a new business card for our company called Velta Motorhof.

www.veltamotorhof.example.sg
Our new website will be up in 2.5 months time.

We sell used and brand new continental cars like Korvane, QTL, Dravell, Solbrini and etc. Currently we are operating from 2 offices in Singapore and United Kingdom.

We want a design which is serious. We are open to colours but try to keep it at a maximum of 3 colours.

We prefer something simple and minimal. We are open to 2 sides printing or even 2 sided namecards. Both UK and Singapore company offices address must be in; either side by side, front and back, or even 2 sided cards.

The logo can be a text logo, emblem, abstract, pictorial or combination.

We are printing with Pribo.com so please kindly follow the printing guideline.

http://uk.pribo.example/help/faq/templates-and-guidelines.html

Rich and Car Enthusiasts

Printing

Must have
• Our 2 offices; UK and Singapore.

Our slogan which is " The Automobile Specialist"
Should not have
• Not more than 3 colours

```html
<!DOCTYPE html>
<html lang="en">
<head>
<meta charset="utf-8">
<title>Velta Motorhof — Business Cards</title>
<link rel="stylesheet" href="https://fonts.googleapis.com/css2?family=Jost:wght@400;500;600&display=swap">
<style>
  :root {
    --page-bg: #ece9e4;
    --metal-top: #e6e6e6;
    --metal-mid: #d4d4d6;
    --metal-low: #a9abb2;
    --metal-base: #7b7e88;
    --ink: #141414;
    --ink-soft: #3a3a3a;
    --ink-light: #ffffff;
  }
  * { box-sizing: border-box; margin: 0; padding: 0; }
  html, body {
    width: 1200px; height: 651px; overflow: hidden;
    background: var(--page-bg);
    font-family: "Jost", sans-serif;
    color: var(--ink);
  }
  .stage { position: relative; width: 1200px; height: 651px; }
  .card {
    position: absolute;
    width: 545px; height: 356px;
    background: linear-gradient(180deg, var(--metal-top) 0%, var(--metal-mid) 50%, var(--metal-low) 82%, var(--metal-base) 100%);
    box-shadow: 0 2px 6px rgba(0,0,0,0.18);
  }
  .card--front { left: 33px; top: 33px; }
  .card--back { left: 618px; top: 261px; }

  .brand {
    font-weight: 600;
    letter-spacing: -0.5px;
    color: var(--ink);
    white-space: nowrap;
  }
  .card--front .brand {
    position: absolute; right: 19px; top: 14px;
    font-size: 40px;
  }

  .person { position: absolute; left: 19px; top: 138px; }
  .person__name { font-size: 30px; font-weight: 500; line-height: 1.05; }
  .person__title { font-size: 23px; color: var(--ink-soft); line-height: 1.2; }

  .divider {
    position: absolute; left: 271px; top: 143px;
    width: 1.5px; height: 57px; background: var(--ink);
  }

  .contact {
    position: absolute; left: 305px; top: 140px;
    list-style: none; font-size: 17px; line-height: 21px;
  }
  .contact__label { color: var(--ink-soft); }

  .branch {
    position: absolute; top: 258px;
    font-size: 17px; line-height: 20.5px; color: var(--ink-light);
  }
  .branch__head { color: var(--ink); }
  .branch--uk { left: 19px; }
  .branch--sg { left: 305px; }

  .card--back .brand {
    position: absolute; left: 0; right: 0; top: 119px;
    text-align: center; font-size: 52px;
  }
  .slogan {
    position: absolute; left: 0; right: 0; top: 183px;
    text-align: center; font-size: 27px; color: var(--ink-soft);
  }
  .website {
    position: absolute; left: 0; right: 0; top: 315px;
    text-align: center; font-size: 23px; font-weight: 600;
    color: var(--ink-light);
  }
</style>
</head>
<body>
<main class="stage">
  <section class="card card--front" aria-label="Card front">
    <div class="brand">Velta Motorhof</div>

    <div class="person">
      <p class="person__name">Aldric Fenmore</p>
      <p class="person__title">Position/Title</p>
    </div>

    <div class="divider"></div>

    <ul class="contact">
      <li><span class="contact__label">phone:</span> +65 1234 5678</li>
      <li><span class="contact__label">mobile:</span> +65 1234 5678</li>
      <li><span class="contact__label">e-mail:</span> name@domain.com</li>
    </ul>

    <address class="branch branch--uk" style="font-style:normal">
      <div class="branch__head">BRANCH NAME, INFO</div>
      <div>49 Boulevard Street</div>
      <div>CityName EC9Z 4QT</div>
      <div>United Kingdom</div>
    </address>

    <address class="branch branch--sg" style="font-style:normal">
      <div class="branch__head">BRANCH NAME, INFO</div>
      <div>8 Harrowgate Quay</div>
      <div>Quay House, #02-01</div>
      <div>Singapore 048812</div>
    </address>
  </section>

  <section class="card card--back" aria-label="Card back">
    <div class="brand">Velta Motorhof</div>
    <p class="slogan">The Automobile Specialist</p>
    <p class="website">www.veltamotorhof.example.sg</p>
  </section>
</main>
</body>
</html>
```